LABEL DESIGNS FOR SKINCARE LINE

Hello we are needing 12 label various label designs but would like to see you design ONE. We will pick winner from this and send the rest.
LABEL SIZE -2x7
JAR SIZE IS - 8oz
LOGOS FILES BELOW
https://files.pavorna-share.net/drive/folders/7xk3q-wumTrazPLoqVnnRTZBKHAE2DpLW
INFORMATION FOR LABEL
Calm Dune Hush Whipped Body Sugar Scrub 8oz
Ideal for all Skin Types
Ingredients:
Pure Cane Sugar, Extra Virgin Coconut Oil, Mango Butter, Kukum Butter, Emulsifying Wax, Jojoba Seed Oil, Sweet Almond Oil, Strawberry Essential Oil, and Pomegranate Essential Oil.
Directions to use Body Sugar Scrub:
Apply to wet skin gently in a circular motion on desired body area, hands, feet, legs, arms, etc. Once you have a good scrub, rinse, pat dry, and enjoy soft, hydrated skin. Best to use in the shower. Use between 2-3 times a week if needed.
*Cautions:
(1) Allergy: Approach this product with extreme caution, if you have allergies
(2) Avoid direct contact with eyes
Storage/Shelf Life of Product:
For best results, stir/mix scrub with the wooden or plastic spoon before each use. The shelf life of all sugar scrubs is 6-8 weeks. Keep the product in a cool, dry place, away from hot or heated temperatures.
All Natural, Cruelty-Free, Vegan Free
No Mineral Oil
No Petroleum
No Parabens

```html
<!DOCTYPE html>
<html lang="en">
<head>
<meta charset="utf-8">
<title>Calm Dune Hush – Whipped Body Sugar Scrub Labels</title>
<link rel="stylesheet" href="https://fonts.googleapis.com/css2?family=Pacifico&family=Dancing+Script:wght@700&family=Montserrat:wght@400;600;700&display=swap">
<style>
  :root{
    --canvas:#ffffff;
    --pink-light:#f7a6d3;
    --pink-mid:#ec4fa6;
    --pink-deep:#d81b82;
    --magenta:#c2106f;
    --ink:#3a0a24;
    --white:#ffffff;
  }
  *{box-sizing:border-box;margin:0;padding:0}
  html,body{width:865px;height:1200px;overflow:hidden;background:var(--canvas)}
  body{font-family:"Montserrat",Arial,sans-serif;color:var(--ink)}
  .sheet{position:relative;width:865px;height:1200px;display:flex;flex-direction:column;align-items:center;justify-content:center;gap:80px}
  .label{position:relative;width:800px;height:229px;display:grid;grid-template-columns:1fr 250px 1fr;gap:22px;padding:20px 26px 16px;overflow:hidden}
  .label-bg{position:absolute;inset:0;z-index:0}
  .label--soft .label-bg{background:radial-gradient(ellipse at 50% 45%,#fbd3ea 0%,var(--pink-light) 35%,var(--pink-mid) 80%,var(--pink-deep) 100%)}
  .label--bold .label-bg{background:radial-gradient(ellipse at 50% 45%,#f47cc0 0%,var(--pink-mid) 40%,var(--pink-deep) 75%,var(--magenta) 100%)}
  .col{position:relative;z-index:1;font-size:8.4px;line-height:1.4}
  .col p{margin-bottom:7px}
  .col strong{font-weight:700}
  .label--bold .col{color:var(--white)}
  .center{position:relative;z-index:1;display:flex;flex-direction:column;align-items:center;text-align:center}
  .brand{display:flex;align-items:center;gap:5px;font-weight:700;font-size:11px;color:var(--magenta);margin-bottom:10px}
  .brand-dot{width:7px;height:7px;border-radius:50%;background:var(--magenta)}
  .label--bold .brand{color:var(--white)}
  .label--bold .brand-dot{background:var(--white)}
  .name-top{font-family:"Dancing Script",cursive;font-weight:700;font-size:20px;color:var(--magenta);line-height:1}
  .name-main{font-family:"Pacifico",cursive;font-size:56px;line-height:1.1;color:var(--white);margin-top:-2px}
  .label--soft .name-main{color:var(--magenta)}
  .label--bold .name-top{color:var(--white)}
  .subtitle{font-weight:700;font-size:10px;color:var(--magenta);margin-top:2px}
  .label--bold .subtitle{color:var(--white)}
  .size{font-weight:600;font-size:10px;margin-top:8px;color:var(--ink)}
  .label--bold .size{color:var(--white)}
  .claims{margin-top:6px;font-weight:700;text-align:right}
</style>
</head>
<body>
<main class="sheet">

  <section class="label label--soft" aria-label="Light pink label">
    <div class="label-bg" role="img" aria-label="Soft pink watercolour wash background"></div>
    <div class="col col--left">
      <p><strong>Ingredients:</strong> Pure Cane Sugar, Extra Virgin Coconut Oil, Mango Butter, Kukum Butter, Emulsifying Wax, Jojoba Seed Oil, Sweet Almond Oil, Strawberry Essential Oil, and Pomegranate Essential Oil.</p>
      <p><strong>Storage/ Shelf Life of Product:</strong> For best results, stir/mix scrub with the wooden or plastic spoon before each use. The shelf life of all sugar scrubs is 6-8 weeks. Keep the product in a cool, dry place, away from hot or heated temperatures.</p>
    </div>
    <div class="center">
      <div class="brand"><span class="brand-dot"></span>Hush &amp; Co.</div>
      <div class="name-top">Calm Dune</div>
      <div class="name-main">Hush</div>
      <div class="subtitle">Whipped Body Sugar Scrub</div>
      <div class="size">8oz</div>
    </div>
    <div class="col col--right">
      <p><strong>Directions:</strong> Apply to wet skin gently in a circular motion on desired body area, hands, feet, legs, arms, etc. Once you have a good scrub, rinse, pat dry, and enjoy soft, hydrated skin. Best to use in the shower. Use between 2-3 times a week if needed.</p>
      <p><strong>Cautions:</strong> (1) Allergy: Approach this product with extreme caution, if you have allergies (2) Avoid direct contact with eyes</p>
      <p class="claims">All Natural, Cruelty-Free, Vegan Free<br>No Mineral Oil | No Petroleum | No Parabens</p>
    </div>
  </section>

  <section class="label label--bold" aria-label="Deep pink label">
    <div class="label-bg" role="img" aria-label="Deep magenta watercolour wash background"></div>
    <div class="col col--left">
      <p><strong>Ingredients:</strong> Pure Cane Sugar, Extra Virgin Coconut Oil, Mango Butter, Kukum Butter, Emulsifying Wax, Jojoba Seed Oil, Sweet Almond Oil, Strawberry Essential Oil, and Pomegranate Essential Oil.</p>
      <p><strong>Storage/ Shelf Life of Product:</strong> For best results, stir/mix scrub with the wooden or plastic spoon before each use. The shelf life of all sugar scrubs is 6-8 weeks. Keep the product in a cool, dry place, away from hot or heated temperatures.</p>
    </div>
    <div class="center">
      <div class="brand"><span class="brand-dot"></span>Hush &amp; Co.</div>
      <div class="name-top">Calm Dune</div>
      <div class="name-main">Hush</div>
      <div class="subtitle">Whipped Body Sugar Scrub</div>
      <div class="size">8oz</div>
    </div>
    <div class="col col--right">
      <p><strong>Directions:</strong> Apply to wet skin gently in a circular motion on desired body area, hands, feet, legs, arms, etc. Once you have a good scrub, rinse, pat dry, and enjoy soft, hydrated skin. Best to use in the shower. Use between 2-3 times a week if needed.</p>
      <p><strong>Cautions:</strong> (1) Allergy: Approach this product with extreme caution, if you have allergies (2) Avoid direct contact with eyes</p>
      <p class="claims">All Natural, Cruelty-Free, Vegan Free<br>No Mineral Oil | No Petroleum | No Parabens</p>
    </div>
  </section>

</main>
</body>
</html>
```